Ridgeway Auto Care
Ridgeway Auto Care - Automotive
Creative Brief
Professional
Dale Morrow
President
4817 Silver Fern Ln Braselton,GA 30519
d.morrow@ridgewayautocare.example
www.ridgewayautocare.example

```html
<!DOCTYPE html>
<html lang="en">
<head>
<meta charset="utf-8">
<title>Ridgeway Auto Care — Stationery Set</title>
<link rel="stylesheet" href="https://fonts.googleapis.com/css2?family=Cinzel:wght@600&family=Open+Sans:wght@400;700&display=swap">
<style>
:root{
  --bg:#f5c4c6;
  --red:#c8202a;
  --red-dark:#9e1820;
  --grey:#8b8b8e;
  --grey-light:#b9b9bc;
  --black:#1e1e1e;
  --paper:#ffffff;
  --ink:#3a3a3a;
}
*{box-sizing:border-box;margin:0;padding:0}
html,body{width:1200px;height:971px;overflow:hidden}
body{background:var(--bg);font-family:"Open Sans",sans-serif;color:var(--ink);position:relative}
.item{position:absolute;box-shadow:0 4px 10px rgba(120,40,45,.25);overflow:hidden}
.paper{background:var(--paper)}
.red{background:var(--red)}
.greyc{background:var(--grey)}
.brand{display:flex;flex-direction:column;align-items:center;gap:4px}
.brand-dot{border-radius:50%;background:currentColor}
.brand-name{font-family:"Cinzel",serif;font-weight:600;letter-spacing:1px;text-align:center;line-height:1.1}
.on-red{color:#fff}
.on-paper{color:var(--grey)}
.swoosh{position:absolute;left:0;right:0;bottom:0}
.swoosh .r{position:absolute;inset:0;background:var(--red);clip-path:polygon(0 40%,62% 40%,70% 0,100% 0,100% 100%,0 100%)}
.swoosh .g{position:absolute;inset:0;background:var(--grey);clip-path:polygon(70% 0,100% 0,100% 100%,64% 100%)}
.swoosh.on-redbg .r{background:var(--paper)}
.contact{font-size:6px;line-height:1.5}
.contact b{color:var(--red);font-size:8px;display:block}

/* business cards */
.card{width:200px;height:114px}
.card-front{left:50px;top:130px}
.card-front .contact{position:absolute;left:12px;top:12px;width:125px}
.card-front .brand{position:absolute;right:10px;top:30px}
.card-red{left:50px;top:256px}
.card-grey{left:50px;top:382px}
.card-red .brand,.card-grey .brand{position:absolute;inset:0;justify-content:center}

/* letterhead */
.letterhead{left:285px;top:50px;width:230px;height:320px}
.letterhead .brand{position:absolute;left:12px;top:14px}
.letterhead .contact{position:absolute;right:14px;top:16px;width:120px}

/* small cards */
.mini{width:150px;height:86px}
.mini-1{left:540px;top:50px}
.mini-2{left:540px;top:150px}
.mini-1 .contact{position:absolute;left:10px;top:10px}
.mini-2 .brand{position:absolute;inset:0;justify-content:center}

/* DL envelope */
.dl{left:540px;top:252px;width:260px;height:118px}
.dl .brand{position:absolute;right:16px;top:14px}

/* envelope stack */
.env{width:300px;height:92px;left:840px}
.env-1{top:50px}
.env-2{top:155px}
.env-3{top:260px}
.env .brand{position:absolute;left:0;right:0;top:8px}
.env .flap{position:absolute;left:0;right:0;bottom:0;height:46px;clip-path:polygon(0 0,50% 100%,100% 0,100% 100%,0 100%)}

/* folder */
.folder{position:absolute;left:40px;top:500px;width:600px;height:470px}
.folder svg{position:absolute;left:0;top:0}
.folder .brand{position:absolute;left:290px;top:70px}
.folder .contact{position:absolute;left:100px;top:350px}
.folder-card{position:absolute;left:330px;top:345px;width:120px;height:68px;background:var(--red);box-shadow:0 2px 5px rgba(0,0,0,.25)}
.folder-card .brand{position:absolute;inset:0;left:0;top:0;justify-content:center}

/* CD */
.cd{position:absolute;left:690px;top:470px;width:150px;height:150px}
.sleeve{left:690px;top:650px;width:190px;height:190px}
.sleeve .brand{position:absolute;inset:0;justify-content:center}

/* fax */
.fax{left:910px;top:420px;width:250px;height:340px}
.fax h1{position:absolute;left:18px;top:44px;font-size:26px;font-weight:700;color:var(--black)}
.fax .contact{position:absolute;right:16px;top:14px}
.fax-fields{position:absolute;left:18px;right:18px;top:92px;display:grid;grid-template-columns:1fr 1fr;gap:9px 12px;font-size:7px}
.fax-fields span{border-bottom:1px solid #999;padding-bottom:2px}
.fax-checks{position:absolute;left:18px;right:18px;top:178px;display:flex;gap:8px;font-size:6px}
.fax-checks span::before{content:"";display:inline-block;width:5px;height:5px;border:1px solid #777;margin-right:2px;vertical-align:middle}
.fax-rule{position:absolute;left:18px;right:18px;top:196px;border-top:1px solid var(--red)}
</style>
</head>
<body>

<!-- Business card, white front -->
<div class="item paper card card-front">
  <div class="contact"><b>Dale Morrow</b>President<br>4817 Silver Fern Ln Braselton,GA 30519<br>Tel: 706-555-0142<br>d.morrow@ridgewayautocare.example</div>
  <div class="brand on-paper"><span class="brand-dot" style="width:18px;height:18px"></span><span class="brand-name" style="font-size:8px">Ridgeway<br>Auto Care</span></div>
  <div class="swoosh" style="height:14px"><div class="r"></div><div class="g"></div></div>
</div>

<!-- Business card, red back -->
<div class="item red card card-red">
  <div class="brand on-red"><span class="brand-dot" style="width:20px;height:20px"></span><span class="brand-name" style="font-size:10px">Ridgeway<br>Auto Care</span></div>
  <div class="swoosh on-redbg" style="height:12px"><div class="r"></div><div class="g"></div></div>
</div>

<!-- Business card, grey -->
<div class="item greyc card card-grey">
  <div class="brand on-red"><span class="brand-dot" style="width:20px;height:20px"></span><span class="brand-name" style="font-size:10px">Ridgeway<br>Auto Care</span></div>
</div>

<!-- Letterhead -->
<div class="item paper letterhead">
  <div class="brand on-paper"><span class="brand-dot" style="width:18px;height:18px"></span><span class="brand-name" style="font-size:7px">Ridgeway<br>Auto Care</span></div>
  <div class="contact">4817 Silver Fern Ln Braselton,GA 30519<br>Tel: 706-555-0142<br>d.morrow@ridgewayautocare.example<br>www.ridgewayautocare.example</div>
  <div class="swoosh" style="height:18px"><div class="r"></div><div class="g"></div></div>
</div>

<!-- Small cards -->
<div class="item paper mini mini-1">
  <div class="contact"><b>Dale Morrow</b>President<br>d.morrow@ridgewayautocare.example<br>www.ridgewayautocare.example</div>
  <div class="swoosh" style="height:10px"><div class="r"></div><div class="g"></div></div>
</div>
<div class="item red mini mini-2">
  <div class="brand on-red"><span class="brand-dot" style="width:14px;height:14px"></span><span class="brand-name" style="font-size:8px">Ridgeway Auto Care</span></div>
</div>

<!-- DL envelope -->
<div class="item red dl">
  <div class="brand on-red"><span class="brand-dot" style="width:16px;height:16px"></span><span class="brand-name" style="font-size:7px">Ridgeway Auto Care</span></div>
  <div class="swoosh on-redbg" style="height:16px"><div class="r" style="background:var(--red-dark)"></div><div class="g"></div></div>
</div>

<!-- Envelope stack -->
<div class="item paper env env-1">
  <div class="brand on-paper"><span class="brand-dot" style="width:14px;height:14px"></span><span class="brand-name" style="font-size:6px">Ridgeway Auto Care</span></div>
  <div class="flap" style="background:var(--red)"></div>
</div>
<div class="item paper env env-2">
  <div class="brand on-paper"><span class="brand-dot" style="width:14px;height:14px"></span><span class="brand-name" style="font-size:6px">Ridgeway Auto Care</span></div>
  <div class="flap" style="background:var(--grey)"></div>
</div>
<div class="item paper env env-3">
  <div class="brand on-paper"><span class="brand-dot" style="width:14px;height:14px"></span><span class="brand-name" style="font-size:6px">Ridgeway Auto Care</span></div>
  <div class="flap" style="background:var(--black)"></div>
</div>

<!-- Presentation folder -->
<div class="folder">
  <svg width="600" height="470" viewBox="0 0 600 470" aria-hidden="true">
    <polygon points="0,40 80,20 80,300 0,280" fill="var(--grey-light)"/>
    <rect x="80" y="20" width="480" height="280" fill="var(--red)"/>
    <polygon points="400,300 430,270 560,270 560,300" fill="var(--grey)"/>
    <polygon points="80,300 560,300 540,420 100,420" fill="var(--paper)"/>
    <polygon points="200,420 260,420 250,470 210,470" fill="var(--paper)"/>
    <polygon points="380,300 560,300 560,318 370,318" fill="var(--grey)"/>
  </svg>
  <div class="brand on-red"><span class="brand-dot" style="width:60px;height:60px"></span><span class="brand-name" style="font-size:22px">Ridgeway<br>Auto Care</span></div>
  <div class="contact">4817 Silver Fern Ln Braselton,GA 30519<br>Tel: 706-555-0142<br>www.ridgewayautocare.example</div>
  <div class="folder-card">
    <div class="brand on-red"><span class="brand-dot" style="width:12px;height:12px"></span><span class="brand-name" style="font-size:6px">Ridgeway Auto Care</span></div>
  </div>
</div>

<!-- CD -->
<svg class="cd" viewBox="0 0 150 150" aria-hidden="true">
  <defs><clipPath id="disc"><circle cx="75" cy="75" r="73"/></clipPath></defs>
  <g clip-path="url(#disc)">
    <rect x="0" y="0" width="150" height="150" fill="var(--red)"/>
    <polygon points="0,85 150,70 150,150 0,150" fill="var(--grey)"/>
  </g>
  <circle cx="75" cy="75" r="14" fill="var(--bg)"/>
  <circle cx="75" cy="38" r="10" fill="#fff"/>
</svg>

<!-- CD sleeve -->
<div class="item red sleeve">
  <div class="brand on-red"><span class="brand-dot" style="width:34px;height:34px"></span><span class="brand-name" style="font-size:14px">Ridgeway<br>Auto Care</span></div>
  <div class="swoosh on-redbg" style="height:16px"><div class="r"></div><div class="g"></div></div>
</div>

<!-- Fax sheet -->
<div class="item paper fax">
  <div class="contact">4817 Silver Fern Ln Braselton,GA 30519<br>Tel: 706-555-0142<br>Fax: 706-555-0143</div>
  <h1>Fax</h1>
  <div class="fax-fields">
    <span>To:</span><span>From:</span>
    <span>Fax:</span><span>Pages:</span>
    <span>Phone:</span><span>Date:</span>
    <span>Re:</span><span>CC:</span>
  </div>
  <div class="fax-checks"><span>Urgent</span><span>For Review</span><span>Please Comment</span><span>Please Reply</span></div>
  <div class="fax-rule"></div>
</div>

</body>
</html>
```